Logo-Design für
lorvem
Zielgruppe
Chinesische Medizin, Akkupunktur
Adresse:
PKR Heilhaus Wiesbaden
Praxis für Chinesische Medizin
Meret Solva | Heilpraktikerin
Lindenhang 7
65191 Wiesbaden
Aufgabenstellung
Logo soll weitgehend beibehalten - ebenso die Farbgebung
sowie die bezeichung für einen Chinesischen Arzt: 中医
Auf der Rückseite der Visitenkarten sollte stehen:
"Ihr nächster Termin:___________"
Die gesamte Rückseite der Visitenkarten nutzen.
Benötigt wird das Logo, Breifpapier, Visitenkarten.

```html
<!DOCTYPE html>
<html lang="de">
<head>
<meta charset="utf-8">
<title>PKR Heilhaus Wiesbaden – Geschäftsausstattung</title>
<link rel="stylesheet" href="https://fonts.googleapis.com/css2?family=Montserrat:wght@500;600;700&family=Mulish:wght@400;600;700&family=Dancing+Script:wght@500&display=swap">
<style>
  :root {
    --green: #1f7a32;
    --green-dark: #176428;
    --field: #d6e8de;
    --ink: #4a4a4a;
    --ink-soft: #777;
    --paper: #ffffff;
    --stage: #e8e7e7;
    --ghost: rgba(0,0,0,0.035);
  }
  * { margin: 0; padding: 0; box-sizing: border-box; }
  html, body { width: 848px; height: 1200px; overflow: hidden; }
  body {
    background: var(--stage);
    position: relative;
    font-family: "Mulish", sans-serif;
    color: var(--ink);
  }
  .card, .letter {
    position: absolute;
    background: var(--paper);
    overflow: hidden;
    box-shadow: 0 2px 6px rgba(0,0,0,0.08);
  }
  .card { width: 384px; height: 248px; top: 50px; }
  .card--front { left: 28px; }
  .card--back { left: 436px; }

  .brand-name {
    font-family: "Montserrat", sans-serif;
    font-weight: 600;
    color: var(--green);
    text-transform: uppercase;
    letter-spacing: 1.2px;
    white-space: nowrap;
  }
  .brand-tagline { color: var(--ink-soft); white-space: nowrap; }
  .brand-dot { background: var(--green); border-radius: 50%; position: absolute; }
  .ghost-circle { position: absolute; border-radius: 50%; background: var(--ghost); }

  /* Front of business card */
  .card--front .ghost-circle { width: 210px; height: 210px; left: 120px; top: 30px; }
  .card--front .brand-dot { width: 84px; height: 84px; right: 24px; top: 16px; }
  .card--front .lockup { position: absolute; left: 26px; top: 44px; }
  .card--front .brand-name { font-size: 15px; }
  .card--front .brand-tagline { font-size: 9.5px; margin-top: 3px; padding-left: 2px; }
  .person { position: absolute; left: 26px; top: 134px; line-height: 1.35; }
  .person__name { font-family: "Montserrat", sans-serif; font-weight: 700; color: var(--green); font-size: 15px; }
  .person__role { font-size: 10px; margin-bottom: 6px; }
  .person__practice { font-family: "Montserrat", sans-serif; font-weight: 600; color: var(--green); font-size: 10.5px; }
  .person__line { font-size: 10.5px; }
  .contact { position: absolute; right: 22px; top: 150px; list-style: none; font-size: 10px; line-height: 1.9; }
  .contact li { display: flex; align-items: center; gap: 7px; }
  .contact svg { width: 9px; height: 9px; fill: var(--green); flex: none; }

  /* Back of business card */
  .card--back .ghost-circle { width: 180px; height: 180px; left: 180px; top: 70px; }
  .appointment-title {
    position: absolute; left: 22px; top: 50px;
    font-family: "Montserrat", sans-serif; font-weight: 700;
    color: var(--green); font-size: 12px; letter-spacing: 2.2px;
  }
  .card--back .lockup { position: absolute; right: 20px; top: 14px; width: 150px; text-align: center; }
  .card--back .brand-dot { width: 26px; height: 26px; left: 62px; top: 0; }
  .card--back .brand-name { font-size: 8px; margin-top: 30px; letter-spacing: 0.6px; }
  .card--back .brand-tagline { font-size: 5.5px; }
  .slots { position: absolute; left: 22px; top: 84px; right: 20px; list-style: none; }
  .slot { display: flex; align-items: center; height: 31px; }
  .slot__days { width: 118px; font-size: 9.5px; letter-spacing: 0.4px; word-spacing: 7px; }
  .slot__field {
    background: var(--field); height: 20px; font-size: 6.5px; color: var(--ink-soft);
    padding: 3px 5px; margin-right: 10px;
  }
  .slot__field--date { width: 118px; }
  .slot__field--time { width: 86px; margin-right: 0; }

  /* Letterhead */
  .letter { left: 28px; top: 350px; width: 480px; height: 690px; font-size: 8.4px; line-height: 1.45; }
  .letter .ghost-circle { width: 300px; height: 300px; left: 90px; top: 420px; }
  .letter .lockup { position: absolute; top: 34px; left: 0; right: 0; text-align: center; }
  .letter .brand-dot { width: 46px; height: 46px; left: 217px; top: 0; }
  .letter .brand-name { font-size: 13px; margin-top: 54px; }
  .letter .brand-tagline { font-size: 8.5px; }
  .recipient { position: absolute; left: 58px; top: 160px; font-size: 7.5px; }
  .date { position: absolute; right: 60px; top: 222px; font-size: 9px; }
  .letter-body { position: absolute; left: 58px; top: 290px; width: 300px; }
  .letter-body .subject { font-size: 10px; font-weight: 600; margin-bottom: 18px; }
  .letter-body p { margin-bottom: 10px; }
  .signature { font-family: "Dancing Script", cursive; color: var(--green); font-size: 17px; margin-top: 8px; }
  .letter-footer {
    position: absolute; right: 40px; bottom: 60px; text-align: right;
    font-size: 6px; line-height: 1.5; color: var(--ink);
  }
  .letter-footer strong { color: var(--green); font-weight: 700; }
  .letter-footer .gap { margin-top: 6px; }

  /* Logo presentation */
  .logo-lockup { position: absolute; left: 528px; top: 400px; width: 292px; text-align: center; }
  .logo-lockup .brand-dot { position: static; display: block; width: 92px; height: 92px; margin: 0 auto 26px; }
  .logo-lockup .brand-name { font-size: 17px; letter-spacing: 1.6px; }
  .logo-lockup .brand-tagline { font-size: 11.5px; margin-top: 6px; letter-spacing: 0.3px; }
  .logo-emblem { position: absolute; left: 540px; top: 660px; width: 280px; height: 280px; }
</style>
</head>
<body>

  <!-- Business card, front -->
  <section class="card card--front">
    <div class="ghost-circle"></div>
    <div class="brand-dot"></div>
    <div class="lockup">
      <div class="brand-name">PKR Heilhaus Wiesbaden</div>
      <div class="brand-tagline">Praxis für Chinesische Medizin</div>
    </div>
    <div class="person">
      <div class="person__name">Meret Solva</div>
      <div class="person__role">Heilpraktikerin</div>
      <div class="person__practice">PKR Heilhaus Wiesbaden</div>
      <div class="person__line">Lindenhang 7</div>
      <div class="person__line">65191 Wiesbaden</div>
    </div>
    <ul class="contact">
      <li><svg viewBox="0 0 10 10"><circle cx="5" cy="5" r="4.5" fill="none" stroke="#1f7a32" stroke-width="1"/><path d="M0.5 5h9M5 0.5c-2.4 2.6-2.4 6.4 0 9M5 0.5c2.4 2.6 2.4 6.4 0 9" fill="none" stroke="#1f7a32" stroke-width="0.8"/></svg>www.pkr-heilhaus.de</li>
      <li><svg viewBox="0 0 10 10"><text x="0" y="8.6" font-size="10" font-family="Mulish, sans-serif" font-weight="700" fill="#1f7a32">@</text></svg>kontakt@pkr-heilhaus.de</li>
      <li><svg viewBox="0 0 10 10"><path d="M2.2 0.6l1.6 2.2-1 1.2c.6 1.3 1.6 2.3 2.9 2.9l1.2-1 2.2 1.6-.9 1.8C4.6 9.2.8 5.4 .4 1.5z"/></svg>+49 (0) 160 98 765 43</li>
    </ul>
  </section>

  <!-- Business card, back -->
  <section class="card card--back">
    <div class="ghost-circle"></div>
    <div class="lockup">
      <div class="brand-dot"></div>
      <div class="brand-name">PKR Heilhaus Wiesbaden</div>
      <div class="brand-tagline">Praxis für Chinesische Medizin</div>
    </div>
    <div class="appointment-title">IHR NÄCHSTER TERMIN...</div>
    <ul class="slots">
      <li class="slot"><span class="slot__days">Mo Di Mi Do Fr</span><span class="slot__field slot__field--date">Datum</span><span class="slot__field slot__field--time">Uhrzeit</span></li>
      <li class="slot"><span class="slot__days">Mo Di Mi Do Fr</span><span class="slot__field slot__field--date">Datum</span><span class="slot__field slot__field--time">Uhrzeit</span></li>
      <li class="slot"><span class="slot__days">Mo Di Mi Do Fr</span><span class="slot__field slot__field--date">Datum</span><span class="slot__field slot__field--time">Uhrzeit</span></li>
      <li class="slot"><span class="slot__days">Mo Di Mi Do Fr</span><span class="slot__field slot__field--date">Datum</span><span class="slot__field slot__field--time">Uhrzeit</span></li>
      <li class="slot"><span class="slot__days">Mo Di Mi Do Fr</span><span class="slot__field slot__field--date">Datum</span><span class="slot__field slot__field--time">Uhrzeit</span></li>
    </ul>
  </section>

  <!-- Letterhead -->
  <section class="letter">
    <div class="ghost-circle"></div>
    <div class="lockup">
      <div class="brand-dot"></div>
      <div class="brand-name">PKR Heilhaus Wiesbaden</div>
      <div class="brand-tagline">Praxis für Chinesische Medizin</div>
    </div>
    <address class="recipient" style="font-style:normal">
      Herrn<br>Jonas Beispiel<br>Beispielweg 12<br>D - 54321 Beispielstadt
    </address>
    <div class="date">26.07.2016</div>
    <div class="letter-body">
      <div class="subject">Lorem ipsum</div>
      <p>Sehr geehrte Damen und Herren,</p>
      <p>Lorem ipsum dolor sit amet, consectetuer adipiscing elit. Aenean commodo ligula eget dolor. Aenean massa. Cum sociis natoque penatibus et magnis dis parturient montes, nascetur ridiculus mus. Donec quam felis, ultricies nec, pellentesque eu, pretium quis, sem. Nulla consequat massa quis enim. Donec pede justo, fringilla vel, aliquet nec, vulputate eget, arcu. In enim justo, rhoncus ut, imperdiet a, venenatis vitae, justo. Nullam dictum felis eu pede mollis pretium. Integer tincidunt. Cras dapibus. Vivamus elementum semper nisi. Aenean vulputate eleifend tellus. Aenean leo ligula, porttitor eu, consequat vitae, eleifend ac, enim.</p>
      <p>Aliquam lorem ante, dapibus in, viverra quis, feugiat a, tellus. Phasellus viverra nulla ut metus varius laoreet. Quisque rutrum. Aenean imperdiet. Etiam ultricies nisi vel augue. Curabitur ullamcorper ultricies nisi. Nam eget dui. Etiam rhoncus. Maecenas tempus, tellus eget condimentum rhoncus, sem quam semper libero, sit amet adipiscing sem neque sed ipsum.</p>
      <p>Mit freundlichen Grüßen</p>
      <div class="signature">Meret Solva</div>
    </div>
    <div class="letter-footer">
      <strong>PKR Heilhaus Wiesbaden</strong><br>
      Praxis für Chinesische Medizin<br>
      Lindenhang 7<br>65191 Wiesbaden
      <div class="gap"><strong>Meret Solva</strong><br>Heilpraktikerin</div>
      <div class="gap">www.pkr-heilhaus.de<br>kontakt@pkr-heilhaus.de<br>+49 (0) 160 98 765 43</div>
      <div class="gap"><strong>Rheinbank Wiesbaden</strong><br>IBAN: DE00 1111 2222 3333 4444 55<br>BIC: RHBKDEXXX</div>
      <div class="gap"><strong>Finanzamt Wiesbaden</strong><br>Umsatzsteuer-ID: DE000000000<br>Steuernummer: 000/000/00000</div>
    </div>
  </section>

  <!-- Logo presentation -->
  <section class="logo-lockup">
    <span class="brand-dot"></span>
    <div class="brand-name">PKR Heilhaus Wiesbaden</div>
    <div class="brand-tagline">Praxis für Chinesische Medizin</div>
  </section>
  <svg class="logo-emblem" viewBox="0 0 280 280" aria-hidden="true">
    <circle cx="140" cy="140" r="140" fill="var(--green)"/>
  </svg>

</body>
</html>
```